Website Comps for Famous Southern BBQ Restaurant in Alabama

We need an authentic, brand-focused redesign for a restaurant.

We need an authentic look.
The client really likes this website.
https://pelzerpit.com/

I don't want to see a bunch of crazy colors.
Avoid image sliders on the homepage. I hate those.

Please mockup the following three pages:
Homepage
Interior page (for mockup purposes, you can do an About page)
Menu page

I only need the PSD's; not the website coded.

Here is the current website: www.dunmoresmokehouse.com

https://pelzerpit.com/

Here are some additional stock photos. New photos will be shot, but these may help for your mock-up designs.
https://www.filecrate.net/sh/83kqvtrpe21zwa9/QXM71bTr4-plWnfVoe8KtYjd?dl=0
Updates

I realize we don't have a lot of high-quality photos to work with.Those will be shot.Here are some additional stock photos that may help.https://www.filecrate.net/sh/83kqvtrpe21zwa9/QXM71bTr4-plWnfVoe8KtYjd?dl=0 Added Saturday, June 10, 2017

Target Market(s)

United states

Industry/Entity Type

Restaurant

Number of Pages Required

3 page

Font styles to use
Sans Serif

Colors

Designer to choose colors to be used in the design.

Requirements
Must have
• An authentic look.
• The client really likes this website.
• https://pelzerpit.com/
• It's simple, bold, and vintage at the same time.
• That is what we want.
• Our existing website is
• dunmoresmokehouse.com
Nice to have
• Simplicity. Something that makes the food look good.
• Possibly a background.
• Logo:
• https://www.filecrate.net/s/k58tnwpl3ovza2e/dunmore-smokehouse-ridgeway.png?dl=0
• Here is a sampling of photos for your comps:
• https://www.filecrate.net/sh/61vbqzhoewpxtn4/QLT4b8JKyRmPPwf6c2ZnHUVpe?dl=0
Should not have
• Nothing too busy.
• Not too many colors.
• Keep it simple, authentic, "down home."
• No homepage image sliders.

```html
<!DOCTYPE html>
<html lang="en">
<head>
<meta charset="utf-8">
<title>Dunmore Smokehouse — Home</title>
<link rel="stylesheet" href="https://fonts.googleapis.com/css2?family=Oswald:wght@400;500&family=Open+Sans:wght@400;600&display=swap">
<style>
:root{
  --orange:#f5a01a;
  --brown:#5a1a06;
  --brown-dark:#4a1505;
  --cream:#faebd3;
  --cream-light:#fdf8ef;
  --text:#4a3a30;
  --white:#ffffff;
  --night:#0e0d0c;
}
*{margin:0;padding:0;box-sizing:border-box}
html,body{width:717px;height:1200px;overflow:hidden;background:var(--white)}
body{position:relative;font-family:"Open Sans",Arial,sans-serif;color:var(--text)}
section,header,footer{position:absolute;left:0;width:717px}

/* header */
.site-header{top:0;height:37px;background:var(--white)}
.brand{position:absolute;left:149px;top:4px;display:flex;align-items:center;gap:4px}
.brand-mark{width:9px;height:9px;background:var(--brown)}
.brand-name{font-family:"Oswald",sans-serif;font-weight:500;font-size:9px;color:var(--brown);text-transform:uppercase;line-height:29px}
.main-nav{position:absolute;right:149px;top:10px;display:flex;gap:7px}
.main-nav a{font-family:"Oswald",sans-serif;font-weight:400;font-size:7.4px;color:var(--brown);text-decoration:none;text-transform:uppercase;padding-top:2px}
.main-nav a.active{color:var(--orange);border-top:1px solid var(--orange)}

/* hero */
.hero{top:37px;height:184px;background:linear-gradient(180deg,#0f2236 0%,#1c3450 38%,#6a3a24 62%,#3a2a24 78%,#182a40 100%)}
.hero-title{position:absolute;top:34px;width:100%;text-align:center;font-family:"Oswald",sans-serif;font-weight:500;font-size:13px;color:var(--orange);text-transform:uppercase}

/* about */
.about{top:221px;height:221px;background:linear-gradient(180deg,var(--white) 0%,var(--white) 50%,var(--cream-light) 100%)}
.about h2{position:absolute;left:149px;top:14px;font-family:"Oswald",sans-serif;font-weight:400;font-size:14.5px;color:var(--brown)}
.team{list-style:none}
.member{position:absolute;left:149px;width:236px}
.member h3{font-family:"Oswald",sans-serif;font-weight:400;font-size:9px;line-height:11px;color:var(--orange);display:flex;align-items:center;gap:2px}
.member h3 svg{width:9px;height:5px}
.member p{font-size:5px;line-height:6px;margin-left:10px;margin-top:2px;letter-spacing:-.05px}
.btn-story{position:absolute;left:149px;top:182px;width:61px;height:16px;background:var(--brown);color:var(--white);font-family:"Oswald",sans-serif;font-size:6.4px;text-align:center;line-height:16px;border-radius:2px}
.about-photo{position:absolute;left:390px;top:18px;width:178px;height:180px;border:2px solid var(--orange);background:linear-gradient(160deg,#7a6654 0%,#5a4a3c 45%,#8c8a88 70%,#3a3c48 100%)}
.about-divider{position:absolute;left:190px;top:218px;width:340px;height:6px;border-radius:50%;box-shadow:0 4px 6px rgba(0,0,0,.12)}

/* restaurants */
.restaurants{top:442px;height:166px}
.venue{position:absolute;top:22px;width:88px;height:120px;background:var(--cream);padding:4px}
.venue-inner{width:100%;height:100%;border:1px solid var(--brown);background:var(--cream);text-align:center;padding-top:9px}
.venue h3{font-family:"Oswald",sans-serif;font-weight:500;font-size:6.8px;color:var(--brown);text-transform:uppercase;line-height:8px;height:20px;padding:0 3px;display:flex;align-items:center;justify-content:center}
.venue-photo{width:50px;height:50px;border-radius:50%;border:2px solid var(--orange);margin:5px auto 9px}
.btn-read{display:inline-block;width:57px;height:13px;background:var(--orange);color:var(--white);font-family:"Oswald",sans-serif;font-size:6.4px;line-height:13px;border-radius:1px}

/* street kitchen */
.street{top:608px;height:234px;background:radial-gradient(ellipse at 46% 60%,#3a2c22 0%,#1a1512 45%,var(--night) 80%)}
.street-copy{position:absolute;top:92px;width:100%;text-align:center;color:var(--white)}
.street-copy h2{font-family:"Oswald",sans-serif;font-weight:500;font-size:12px}
.street-copy .rule{width:54px;height:1px;background:var(--white);margin:3px auto 6px}
.street-copy p{font-size:8px;line-height:11px}

/* hours */
.hours{top:842px;height:134px}
.hours-card{position:absolute;top:24px;width:87px;height:91px;background:var(--white);border:1px solid #f1e8dc}
.hours-card h3{display:flex;align-items:center;gap:5px;padding:10px 0 0 13px;font-family:"Oswald",sans-serif;font-weight:400;font-size:11px;color:var(--orange)}
.hours-card h3 svg{width:11px;height:10px}
.hours-info{padding:5px 0 0 13px;font-size:5.5px;line-height:7px;color:var(--text)}
.hours-info div{display:flex;gap:2px}
.hours-info svg{width:4px;height:5px;margin-top:1px;flex:none}
.hours-info .phone{margin-top:3px}
.hours-time{position:absolute;left:0;bottom:0;width:100%;height:25px;background:var(--orange);color:var(--white);font-size:5.6px;line-height:7px;display:flex;align-items:center;padding-left:5px;gap:3px}
.hours-time svg{width:5px;height:5px;flex:none}

/* news */
.news{top:976px;height:202px;background:var(--cream)}
.news::before{content:"";position:absolute;left:0;top:-4px;width:100%;height:8px;background:radial-gradient(circle at 4px 8px,var(--cream) 4px,transparent 4.5px) 0 0/8px 8px repeat-x}
.news h2{position:absolute;top:17px;width:100%;text-align:center;font-family:"Oswald",sans-serif;font-weight:400;font-size:14px;color:var(--brown)}
.post{position:absolute;top:50px;width:137px}
.post-photo{width:137px;height:86px}
.post h3{margin-top:7px;font-family:"Oswald",sans-serif;font-weight:400;font-size:8.4px;color:var(--brown)}
.post p{font-size:6.4px;line-height:8.4px;padding-right:4px}

/* footer */
.site-footer{top:1178px;height:22px;background:var(--brown-dark);color:var(--white)}
.copyright{position:absolute;left:149px;top:0;line-height:22px;font-family:"Oswald",sans-serif;font-size:5.6px;text-transform:uppercase}
.footer-nav{position:absolute;right:149px;top:0;display:flex;gap:5px;line-height:22px}
.footer-nav a{color:var(--white);text-decoration:none;font-family:"Oswald",sans-serif;font-size:5.2px;text-transform:uppercase}
</style>
</head>
<body>

<header class="site-header">
  <div class="brand"><span class="brand-mark"></span><span class="brand-name">Dunmore Smokehouse</span></div>
  <nav class="main-nav">
    <a href="#" class="active">Home</a><a href="#">About</a><a href="#">Locations</a><a href="#">Restaurant Menus</a><a href="#">Catering</a><a href="#">News</a><a href="#">Store</a><a href="#">Contact Us</a>
  </nav>
</header>

<section class="hero" role="img" aria-label="Ribs smoking on a long grill over glowing coals">
  <h1 class="hero-title">Pork-Stuffed Tater in “50 Plates to Try in Alabama”</h1>
</section>

<section class="about">
  <h2>About Us</h2>
  <ul class="team">
    <li class="member" style="top:44px"><h3><svg viewBox="0 0 9 5"><path d="M0 2.5h6" stroke="#5a1a06" stroke-width="1"/><circle cx="7" cy="2.5" r="1.8" fill="#5a1a06"/></svg>Carl Pruett</h3>
      <p>Pruett opened his original Dunmore Smokehouse in Ridgeway’s Maple Hill neighborhood in 2009, and opened Dunmore Soul Kitchen with co-owner Wes Harlan in Linden Park.</p></li>
    <li class="member" style="top:82px"><h3><svg viewBox="0 0 9 5"><path d="M0 2.5h6" stroke="#5a1a06" stroke-width="1"/><circle cx="7" cy="2.5" r="1.8" fill="#5a1a06"/></svg>Wes Harlan</h3>
      <p>Former chef de cuisine at Tidewater, is Dunmore Soul Kitchen executive chef and part-owner.</p></li>
    <li class="member" style="top:114px"><h3><svg viewBox="0 0 9 5"><path d="M0 2.5h6" stroke="#5a1a06" stroke-width="1"/><circle cx="7" cy="2.5" r="1.8" fill="#5a1a06"/></svg>Roy Tillman</h3>
      <p>Co-owner of Dunmore Juke Joint, former owner Tillman’s Oysters &amp; Steaks in the same Oakcrest Park shopping center.</p></li>
    <li class="member" style="top:152px"><h3><svg viewBox="0 0 9 5"><path d="M0 2.5h6" stroke="#5a1a06" stroke-width="1"/><circle cx="7" cy="2.5" r="1.8" fill="#5a1a06"/></svg>Dale Mercer</h3>
      <p>Southern Voices winner Mercer was a co-owner of Ember.</p></li>
  </ul>
  <a class="btn-story">Dunmore Story</a>
  <div class="about-photo" role="img" aria-label="Owner seated in the restaurant dining room with vintage signs on the wall"></div>
  <div class="about-divider"></div>
</section>

<section class="restaurants">
  <article class="venue" style="left:194px"><div class="venue-inner">
    <h3>Dunmore Smokehouse-Maple Hill</h3>
    <div class="venue-photo" role="img" aria-label="Storefront of the Maple Hill restaurant" style="background:linear-gradient(160deg,#b8332c,#d8c8b0 55%,#5a5048)"></div>
    <span class="btn-read">Read More</span></div></article>
  <article class="venue" style="left:314px"><div class="venue-inner">
    <h3>Dunmore Soul Kitchen - Linden Park</h3>
    <div class="venue-photo" role="img" aria-label="Restaurant sign against a blue sky" style="background:radial-gradient(circle,#3a3230 0 30%,#4f8ad0 32%,#2f6fc0 100%)"></div>
    <span class="btn-read">Read More</span></div></article>
  <article class="venue" style="left:435px"><div class="venue-inner">
    <h3>Dunmore Juke Joint - Oakcrest</h3>
    <div class="venue-photo" role="img" aria-label="Interior of the Oakcrest restaurant with a flag on the wall" style="background:linear-gradient(180deg,#8c5a3c,#5a3a28 60%,#2c2018)"></div>
    <span class="btn-read">Read More</span></div></article>
</section>

<section class="street" role="img" aria-label="Pitmaster tending a glowing barrel smoker in the dark">
  <div class="street-copy">
    <h2>Dunmore Street Kitchen</h2>
    <div class="rule"></div>
    <p>Dunmore Smokehouse on Wheels...Serving Lunch Daily with Catering for Parties, Events &amp; Just About<br>Anything Else!</p>
  </div>
</section>

<section class="hours">
  <article class="hours-card" style="left:207px">
    <h3><svg viewBox="0 0 11 10"><path d="M0 1.5l3.5-1.5 4 1.5 3.5-1.5v8.5l-3.5 1.5-4-1.5-3.5 1.5z" fill="#5a1a06"/><path d="M3.5 0v8.5M7.5 1.5v8.5" stroke="#fff" stroke-width=".6"/></svg>Location</h3>
    <div class="hours-info">
      <div><svg viewBox="0 0 4 5"><path d="M2 5C.3 3 0 2.3 0 2a2 2 0 014 0c0 .3-.3 1-2 3z" fill="#4a3a30"/></svg><span>2417 Birchline Road<br>Ridgeway AL 35990</span></div>
      <div class="phone"><svg viewBox="0 0 4 5"><path d="M.6 0l1 1.2-.5.8c.3.8.7 1.3 1.3 1.6l.7-.5 1 1-.6.9C1.8 4.8 0 2.4.1.6z" fill="#4a3a30"/></svg><span>(555) 014-2286</span></div>
    </div>
    <div class="hours-time"><svg viewBox="0 0 5 5"><circle cx="2.5" cy="2.5" r="2.2" fill="none" stroke="#fff" stroke-width=".6"/><path d="M2.5 1.2v1.4l1 .6" stroke="#fff" stroke-width=".5" fill="none"/></svg><span>Mon - Sat: 11:00 am - 8 pm</span></div>
  </article>
  <article class="hours-card" style="left:312px">
    <h3><svg viewBox="0 0 11 10"><path d="M0 1.5l3.5-1.5 4 1.5 3.5-1.5v8.5l-3.5 1.5-4-1.5-3.5 1.5z" fill="#5a1a06"/><path d="M3.5 0v8.5M7.5 1.5v8.5" stroke="#fff" stroke-width=".6"/></svg>Location</h3>
    <div class="hours-info">
      <div><svg viewBox="0 0 4 5"><path d="M2 5C.3 3 0 2.3 0 2a2 2 0 014 0c0 .3-.3 1-2 3z" fill="#4a3a30"/></svg><span>2417 Birchline Road<br>Ridgeway AL 35990</span></div>
      <div class="phone"><svg viewBox="0 0 4 5"><path d="M.6 0l1 1.2-.5.8c.3.8.7 1.3 1.3 1.6l.7-.5 1 1-.6.9C1.8 4.8 0 2.4.1.6z" fill="#4a3a30"/></svg><span>(555) 014-2286</span></div>
    </div>
    <div class="hours-time"><svg viewBox="0 0 5 5"><circle cx="2.5" cy="2.5" r="2.2" fill="none" stroke="#fff" stroke-width=".6"/><path d="M2.5 1.2v1.4l1 .6" stroke="#fff" stroke-width=".5" fill="none"/></svg><span>Mon - Sat: 11:00 am - 8 pm<br>Sun: 11:00 am - 4 pm</span></div>
  </article>
  <article class="hours-card" style="left:415px">
    <h3><svg viewBox="0 0 11 10"><path d="M0 1.5l3.5-1.5 4 1.5 3.5-1.5v8.5l-3.5 1.5-4-1.5-3.5 1.5z" fill="#5a1a06"/><path d="M3.5 0v8.5M7.5 1.5v8.5" stroke="#fff" stroke-width=".6"/></svg>Location</h3>
    <div class="hours-info">
      <div><svg viewBox="0 0 4 5"><path d="M2 5C.3 3 0 2.3 0 2a2 2 0 014 0c0 .3-.3 1-2 3z" fill="#4a3a30"/></svg><span>2417 Birchline Road<br>Ridgeway AL 35990</span></div>
      <div class="phone"><svg viewBox="0 0 4 5"><path d="M.6 0l1 1.2-.5.8c.3.8.7 1.3 1.3 1.6l.7-.5 1 1-.6.9C1.8 4.8 0 2.4.1.6z" fill="#4a3a30"/></svg><span>(555) 014-2286</span></div>
    </div>
    <div class="hours-time" style="padding-left:14px"><svg viewBox="0 0 5 5"><circle cx="2.5" cy="2.5" r="2.2" fill="none" stroke="#fff" stroke-width=".6"/><path d="M2.5 1.2v1.4l1 .6" stroke="#fff" stroke-width=".5" fill="none"/></svg><span>Mon - Sat: 11:00 am<br>- 12:00 am/midnight</span></div>
  </article>
</section>

<section class="news">
  <h2>News &amp; Event</h2>
  <article class="post" style="left:149px">
    <div class="post-photo" role="img" aria-label="Tongs turning meat over a smoking grill" style="background:linear-gradient(160deg,#2a2624,#8a8580 45%,#4a3a30 80%)"></div>
    <h3>Best BB Qs</h3>
    <p>Lorem Ipsum is simply dummy text of the printing and typesetting industry. Lorem Ipsum has been the</p>
  </article>
  <article class="post" style="left:290px">
    <div class="post-photo" role="img" aria-label="Rows of ribs on a grill over coals" style="background:linear-gradient(180deg,#13263a,#7a3e26 55%,#2a3448)"></div>
    <h3>Best BB Qs</h3>
    <p>Lorem Ipsum is simply dummy text of the printing and typesetting industry. Lorem Ipsum has been the</p>
  </article>
  <article class="post" style="left:431px">
    <div class="post-photo" role="img" aria-label="Smoked meats on racks inside a smoker" style="background:linear-gradient(180deg,#2a2220,#9a3a24 40%,#3a2a24 70%,#6a5a50)"></div>
    <h3>Best BB Qs</h3>
    <p>Lorem Ipsum is simply dummy text of the printing and typesetting industry. Lorem Ipsum has been the</p>
  </article>
</section>

<footer class="site-footer">
  <p class="copyright">Copyright 2017 Dunmore Smokehouse, LLC</p>
  <nav class="footer-nav">
    <a href="#">Home</a><a href="#">About</a><a href="#">Locations</a><a href="#">Restaurant Menus</a><a href="#">Catering</a><a href="#">News</a><a href="#">Store</a><a href="#">Contact Us</a>
  </nav>
</footer>

</body>
</html>
```